WEb page design for the nations most eco friendly hair salon. Need to be able to link on online salo

Torvan Eco Salon, will be the nations most eco friendly hair salon. Opening In Jacksonville Beach, Florida in December 2015. This will be the first salon in the nation and potentially the world to be, 100% solar powered. eliminating plastics usage by 99%. chemical and ammonia free color, non toxic paint, non vinyl furniture. 99% recycling procedures in place including, all aluminum, cardboard, batteries, lighbulbs, hair clippings, etc...thanks to our partnership with Blue Meadow Studios. This will be a salon where Simplicity and luxury can finally coexist in perfect harmony. We will not only completely eliminate the threat of any future damage done to our planet from this point forward, but we will strive every day to reduce as much damage that has been done by taking every effort necessary to showcase a more beautiful way to take care of the earth and ourselves.

Target Market(s)

middle aged business men and women.

Industry/Entity Type

Hair And Beauty

Coding

Coded - Design and coding required

Number of Pages Required

2 page

Colors
000000

Requirements
Must have
• link to salon online booking software, and maximum 2 charitable foundations that our salon will be involved with as well as instagram and facebook page.
• hours of operation 10am-8pm Monday-Friday
• 10am-6pm Saturdays
Nice to have
• Lumora hair care products
• address 817 lower n 6th st Jacksonville beach fl, 32075
• email lumorastudio@mailvento.net

```html
<!DOCTYPE html>
<html lang="en">
<head>
<meta charset="utf-8">
<title>Torvan Eco Salon</title>
<link href="https://fonts.googleapis.com/css2?family=Roboto:ital,wght@0,300;0,400;0,500;0,700;1,400&display=swap" rel="stylesheet">
<style>
:root{
  --green:#3f8a1c;
  --green-dark:#2f6f10;
  --green-light:#5aa62a;
  --lime:#8cc63f;
  --ink:#222;
  --text:#555;
  --nav:#2b2b2b;
  --btn:#2a2a2a;
  --grey-bg:#f0f0f0;
  --white:#fff;
}
*{margin:0;padding:0;box-sizing:border-box}
html,body{width:1200px;height:2671px;overflow:hidden;background:var(--white)}
body{font-family:"Roboto",Arial,sans-serif;color:var(--text);position:relative}
.abs{position:absolute}
.btn{position:absolute;background:linear-gradient(#3a3a3a,#1f1f1f);color:#fff;font-size:14px;font-weight:500;text-transform:uppercase;display:flex;align-items:center;justify-content:center;border-radius:3px}

/* header */
.site-header{position:absolute;left:0;top:0;width:1200px;height:108px;background:#fff}
.brand{position:absolute;left:75px;top:26px;display:flex;align-items:center;gap:10px}
.brand-dot{width:22px;height:22px;border-radius:50%;background:var(--green-light)}
.brand-name{font-size:30px;font-weight:700;color:var(--green)}
.info-block{position:absolute;top:26px}
.info-block h4{color:var(--green);font-size:15px;font-weight:700;text-transform:uppercase;margin-bottom:8px}
.info-block p{color:#333;font-size:13px;line-height:19px}

.main-nav{position:absolute;left:0;top:108px;width:1200px;height:43px;background:linear-gradient(#3b3b3b,#1e1e1e);display:flex;align-items:center;padding-left:75px;gap:0}
.main-nav a{color:#fff;text-decoration:none;font-size:13.5px;text-transform:uppercase;margin-right:40px}

/* hero */
.hero{position:absolute;left:0;top:151px;width:1200px;height:446px}
.hero-photo{position:absolute;inset:0;background:linear-gradient(180deg,#8fb3c8 0%,#c6d6dc 35%,#9aa7ac 60%,#6f7a80 100%)}
.hero-title{position:absolute;left:75px;top:142px;color:#fff;font-size:39px;font-weight:500;line-height:44px;text-transform:uppercase;text-shadow:0 2px 4px rgba(0,0,0,.35)}
.hero-dots{position:absolute;left:75px;top:259px;display:flex;gap:9px}
.hero-dots span{width:9px;height:9px;border-radius:50%;background:#fff}
.hero-dots span:first-child{background:var(--lime)}
.booking{position:absolute;left:795px;top:61px;width:331px;height:260px;background:#f4f4f4;box-shadow:0 2px 6px rgba(0,0,0,.3)}
.booking h3{height:40px;background:linear-gradient(var(--green-light),var(--green));color:#fff;font-size:21px;font-weight:500;text-transform:uppercase;padding:8px 12px}
.booking .field{margin:8px 16px 0 16px;height:35px;background:#fff;border:1px solid #d5d5d5;font-size:13px;color:#666;padding:10px 14px}
.booking .field:first-of-type{margin-top:14px}
.booking .btn{left:16px;top:187px;width:298px;height:45px;font-size:16px}
.hero-wave{position:absolute;left:0;bottom:0;width:1200px;height:80px}

/* headings */
.sec-title{position:absolute;left:0;width:1200px;text-align:center;font-size:26px;font-weight:400;text-transform:uppercase;color:var(--green)}
.sec-text{position:absolute;left:75px;width:1050px;text-align:center;font-size:13px;line-height:27px;color:var(--text)}

/* services */
.services-band{position:absolute;left:0;top:880px;width:1200px;height:625px}
.service{position:absolute;width:300px;text-align:center;color:#fff}
.service-icon{width:128px;height:128px;border-radius:50%;background:#fff;margin:0 auto;display:flex;align-items:center;justify-content:center}
.service-icon div{width:60px;height:60px;border-radius:50%;background:var(--green-dark)}
.service h5{margin-top:33px;font-size:14.5px;font-weight:700;text-transform:uppercase}
.service p{margin-top:12px;font-size:13px;line-height:21px;padding:0 30px}

/* gallery + testimonials */
.showcase{position:absolute;left:0;top:1764px;width:1200px;height:380px;background:var(--grey-bg)}
.sub-title{position:absolute;font-size:26px;text-transform:uppercase;color:var(--green)}
.thumb{position:absolute;width:157px;height:105px;border-radius:2px}
.divider-v{position:absolute;left:602px;top:56px;width:1px;height:278px;background:#cfcfcf}
.quote-photo{position:absolute;left:633px;width:142px;height:94px}
.quote{position:absolute;left:795px;width:335px}
.quote p{font-style:italic;font-size:13px;line-height:21px;color:#555}
.quote h6{margin-top:8px;font-size:13px;font-weight:700;color:var(--green)}
.divider-h{position:absolute;left:633px;top:220px;width:497px;height:1px;background:#cfcfcf}

/* cta */
.cta-text{position:absolute;left:189px;top:2191px;font-size:23px;color:var(--green)}

/* footer */
.footer-band{position:absolute;left:0;top:2275px;width:1200px;height:336px}
.foot-col{position:absolute;color:#fff}
.foot-col h4{font-size:16px;font-weight:700;text-transform:uppercase;margin-bottom:14px}
.foot-col p{font-size:13px;line-height:21px}
.foot-col strong{font-size:14px}
.foot-col .link{font-size:12px;font-weight:700;text-transform:uppercase;margin-top:14px}
.map{position:absolute;left:319px;top:2375px;width:447px;height:203px;border:3px solid #1d3d0d;background:linear-gradient(135deg,#e8e3d6,#d9e4cf 60%,#c9d8e6)}
.bottom-bar{position:absolute;left:0;top:2611px;width:1200px;height:60px;background:#333}
.bottom-bar p{position:absolute;left:75px;top:22px;font-size:12px;color:#aaa}
.social{position:absolute;top:16px;width:28px;height:28px;border-radius:3px}
</style>
</head>
<body>

<header class="site-header">
  <div class="brand"><span class="brand-dot"></span><span class="brand-name">Torvan Eco Salon</span></div>
  <div class="info-block" style="left:759px">
    <h4>Hours of Operation</h4>
    <p>10am-8pm Monday-Friday<br>10am-6pm Saturdays</p>
  </div>
  <div class="info-block" style="left:964px">
    <h4>Email</h4>
    <p>lumorastudio@mailvento.net</p>
  </div>
</header>

<nav class="main-nav">
  <a>Home</a><a>About Us</a><a>Services</a><a>Gallery</a><a>Why Torvan Eco Salon</a><a>Testimonials</a><a>Blog</a><a>Careers</a><a>Contact Us</a>
</nav>

<section class="hero">
  <div class="hero-photo" role="img" aria-label="Woman meditating on a rocky hillside at sunrise under a blue sky"></div>
  <h1 class="hero-title">We are a first<br>eco salon in Florida</h1>
  <div class="hero-dots"><span></span><span></span><span></span><span></span></div>
  <form class="booking">
    <h3>Get Online Booking</h3>
    <div class="field">Full Name</div>
    <div class="field">Email Address</div>
    <div class="field">Select Services</div>
    <div class="btn">Book an Appointment</div>
  </form>
  <svg class="hero-wave" viewBox="0 0 1200 80" preserveAspectRatio="none">
    <path d="M0,40 C250,70 500,60 750,35 C950,15 1100,20 1200,25 L1200,80 L0,80 Z" fill="#8cc63f"/>
    <path d="M0,55 C250,80 500,72 750,48 C950,30 1100,32 1200,38 L1200,80 L0,80 Z" fill="#3f8a1c"/>
    <path d="M0,68 C250,92 500,82 750,60 C950,42 1100,44 1200,50 L1200,80 L0,80 Z" fill="#fff"/>
  </svg>
</section>

<h2 class="sec-title" style="top:643px">Welcome to Torvan Eco Salon</h2>
<p class="sec-text" style="top:692px">Aliquam molestie, mi et imperdiet euismod, dui purus auctor tellus, et interdum lacus lectus et ante. Sed accumsan sollicitudin sapien, sit amet adipiscing turpis gravida ac. In congue, neque ac lobortis volutpat, libero mauris varius mi, vitae suscipit ipsum ligula vitae risus. Duis aliquam nibh a dui iaculis viverra id a velit. Vivamus egestas risus in magna varius commodo. Sed semper viverra egestas. Etiam pretium porttitor lectus, vel ornare neque porta volutpat.</p>
<div class="btn" style="left:525px;top:804px;width:152px;height:41px">Read More</div>

<svg class="services-band" viewBox="0 0 1200 625" preserveAspectRatio="none">
  <defs><linearGradient id="bandGrad" x1="0" y1="0" x2="0" y2="1"><stop offset="0" stop-color="#2f6f10"/><stop offset="1" stop-color="#4a951f"/></linearGradient></defs>
  <path d="M0,80 C250,20 500,0 700,30 C900,60 1050,60 1200,40 L1200,560 C1000,520 850,600 600,615 C350,630 200,560 0,530 Z" fill="url(#bandGrad)"/>
</svg>
<h2 class="sec-title" style="top:999px;color:#fff">Torvan Eco Salon Services</h2>
<p class="sec-text" style="top:1056px;color:#fff">Aliquam molestie, mi et imperdiet euismod, dui purus auctor tellus, et interdum lacus lectus et ante. Sed accumsan sollicitudin sapien, sit amet adipiscing turpis gravida ac. In congue, neque ac lobortis volutpat, libero mauris varius mi, vitae suscipit ipsum ligula vitae risus.</p>
<div class="service" style="left:90px;top:1149px"><div class="service-icon"><div role="img" aria-label="Leaf service icon"></div></div><h5>Services Heading 1</h5><p>Duis aliquam nibh a dui iaculis viverra id a velit. Vivamus egestas risus in magna varius commodo.</p></div>
<div class="service" style="left:450px;top:1149px"><div class="service-icon"><div role="img" aria-label="Flower service icon"></div></div><h5>Services Heading 1</h5><p>Duis aliquam nibh a dui iaculis viverra id a velit. Vivamus egestas risus in magna varius commodo.</p></div>
<div class="service" style="left:810px;top:1149px"><div class="service-icon"><div role="img" aria-label="Blossom branch service icon"></div></div><h5>Services Heading 1</h5><p>Duis aliquam nibh a dui iaculis viverra id a velit. Vivamus egestas risus in magna varius commodo.</p></div>

<h2 class="sec-title" style="top:1550px">Why Torvan Eco Salon make difference</h2>
<p class="sec-text" style="top:1597px;font-size:16px;line-height:30px">We Used 100% solar powered. eliminating plastics usage by 99%. chemical and ammonia free color, non toxic paint, non vinyl furniture.<br>99% recycling procedures in place including, all aluminum, cardboard, batteries, lightbulbs, hair clippings etc...</p>
<div class="btn" style="left:574px;top:1680px;width:103px;height:41px;left:525px;width:152px">Read More</div>

<section class="showcase">
  <h3 class="sub-title" style="left:113px;top:46px">Photo Gallery</h3>
  <div class="thumb" style="left:75px;top:111px;background:linear-gradient(135deg,#8fae7a,#cbb8a4)" role="img" aria-label="Hands holding natural cream"></div>
  <div class="thumb" style="left:244px;top:111px;background:linear-gradient(135deg,#6b4a36,#b98b62)" role="img" aria-label="Stylist cutting hair"></div>
  <div class="thumb" style="left:413px;top:111px;background:linear-gradient(135deg,#d9d2cc,#f2ece6)" role="img" aria-label="Client with facial treatment"></div>
  <div class="thumb" style="left:75px;top:232px;background:linear-gradient(135deg,#8a5a2e,#d2a36a)" role="img" aria-label="Hair being washed"></div>
  <div class="thumb" style="left:244px;top:232px;background:linear-gradient(135deg,#4a4a4a,#a9a9a9)" role="img" aria-label="Salon interior with stylists"></div>
  <div class="thumb" style="left:413px;top:232px;background:linear-gradient(135deg,#7a5a48,#c89f86)" role="img" aria-label="Eye makeup close-up"></div>
  <div class="divider-v"></div>
  <h3 class="sub-title" style="left:670px;top:46px">What our customer says</h3>
  <div class="quote-photo" style="top:111px;background:linear-gradient(135deg,#5a4a40,#b7a796)" role="img" aria-label="Client being styled"></div>
  <div class="quote" style="top:105px"><p>“ Duis aliquam nibh a dui iaculis viverra id a velit. Vivamus egestas risus in magna varius commodo. Sed semper viverra egestas...</p><h6>-Name Heading</h6></div>
  <div class="divider-h"></div>
  <div class="quote-photo" style="top:242px;background:linear-gradient(135deg,#a27a52,#e0c7a6)" role="img" aria-label="Smiling stylist in salon"></div>
  <div class="quote" style="top:236px"><p>“ Duis aliquam nibh a dui iaculis viverra id a velit. Vivamus egestas risus in magna varius commodo. Sed semper viverra egestas...</p><h6>-Name Heading</h6></div>
</section>

<p class="cta-text">Vestibulum ante ipsum primis in faucibus orci luctus</p>
<div class="btn" style="left:757px;top:2183px;width:241px;height:48px;font-size:16px">Book an Appointment</div>

<svg class="footer-band" viewBox="0 0 1200 336" preserveAspectRatio="none">
  <path d="M0,20 C200,60 450,90 700,60 C900,35 1050,20 1200,30 L1200,336 L0,336 Z" fill="#3f8a1c"/>
</svg>
<div class="foot-col" style="left:75px;top:2372px">
  <h4>Contact Information</h4>
  <p><strong>Torvan Eco Salon</strong><br>817 lower n 6th st Jacksonville<br>Beach Florida, 32075</p>
  <p class="link">Get Direction</p>
</div>
<div class="map" role="img" aria-label="Street map of Jacksonville Beach"></div>
<div class="foot-col" style="left:809px;top:2372px">
  <h4>Hours of Operation</h4>
  <p>10am-8pm Monday-Friday<br>10am-6pm Saturdays</p>
  <h4 style="margin-top:28px">Email</h4>
  <p>lumorastudio@mailvento.net</p>
</div>

<footer class="bottom-bar">
  <p>Copyright © 2015. Company Name All Right Reserved</p>
  <span class="social" style="left:991px;background:#3b5a99"></span>
  <span class="social" style="left:1026px;background:#3fa9d8"></span>
  <span class="social" style="left:1061px;background:#e8731d"></span>
  <span class="social" style="left:1096px;background:#c4302b"></span>
</footer>

</body>
</html>
```